Professional, Attractive, Simple Website Needed!!

We completed the design for our logo.

We need a website built out around this.

Here are a couple samples of how we want ours formatted.

http://brvntapower.com

http://www.halvorbeam.com/lp/free-quote?LeadSource=Search%20Engine&ProgramName=webquery&experience=qual&language=en&type=brd&gclid=Xq7RTPwmEYKDLAvUHbsNQkfPZrTcGwnJuoVbXeLqHmRYdAsWtPkMcNfBYgzTrUoQJhEdWvKpYaLsZbCmNDgQwTxAoKpXbT_qkR

http://morvalo.co

Reason: Extending this deadline due to our delay in providing designers with content for each page. This is coming in next 24 hours.

Reason: Due to scheduling conflicts and extended travel delays related to Puerto Rico, the deadline has been extended. Your patience is greatly appreciated.

Reason: Travel and scheduling conflicts have made it impossible to give this project the thorough review it deserves, therefore I am extending the deadline. Thank you for your patience!

Target Market(s)

Home Owners who earn 60k + household annually

Industry/Entity Type

It Professional

Coding

Coded - Design and coding required

Number of Pages Required

5+ page

Font styles to use
Serif

Colors
34a7d8
9bcb3c

Requirements
Must have
• Simple
• Lead form Entry (Ability for visitor to enter Name, number and address for a quote)
• Sleek Design
• Professional
• Testimonials
• Use color Scheme of Design Logo Attached
Nice to have
• Video when site starts
• Like this
• https://www.vidmarrow.com/watch?v=qT8mRpXw2Ka&feature=vidm.ro
Should not have
• Should not include Commercial solar
• Should not include wind power

```html
<!DOCTYPE html>
<html lang="en">
<head>
<meta charset="utf-8">
<title>Terra Bright Energy</title>
<link rel="stylesheet" href="https://fonts.googleapis.com/css2?family=Kumbh+Sans:wght@400;500;600;700&family=Open+Sans:wght@400;600&family=Raleway:wght@400;600&family=Roboto:wght@400;500;700&display=swap">
<style>
:root{
  --green:#8dc63f;
  --green-deep:#5fb030;
  --yellow:#f3ea1c;
  --blue:#0aa4e6;
  --badge:#1687c9;
  --ink:#222222;
  --muted:#666666;
  --band:#ececec;
  --form-bg:rgba(40,40,40,.94);
  --footer:#1f242c;
  --footer-line:#343a44;
  --footer-text:#7c838d;
  --white:#ffffff;
}
*{margin:0;padding:0;box-sizing:border-box}
html,body{width:1200px;height:2326px;overflow:hidden;background:var(--white)}
body{position:relative;font-family:"Open Sans",sans-serif;color:var(--ink)}
.abs{position:absolute}

/* hero */
.hero-photo{position:absolute;left:0;top:0;width:1200px;height:670px}
.brand{position:absolute;display:flex;align-items:center;gap:10px;font-family:"Kumbh Sans",sans-serif;font-weight:700;color:var(--green)}
.brand-dot{width:26px;height:26px;border-radius:50%;background:var(--blue);flex:none}
.brand-header{left:88px;top:52px;font-size:21px}
.nav{position:absolute;top:53px;left:417px;display:flex;align-items:center;font-family:"Kumbh Sans",sans-serif;font-weight:600;font-size:13px;color:var(--white);text-transform:uppercase}
.nav a{color:inherit;text-decoration:none;height:32px;line-height:32px;padding:0 14px}
.nav a.active{background:var(--green)}
.nav a.contact{margin-left:22px}
.hero-kicker{left:0;width:1200px;top:180px;text-align:center;color:var(--white);font-family:"Kumbh Sans",sans-serif;font-size:20px;font-weight:500}
.hero-title{left:0;width:1200px;top:210px;text-align:center;color:var(--white);font-family:"Kumbh Sans",sans-serif;font-size:52px;font-weight:700}

/* lead form */
.lead-form{left:391px;top:426px;width:424px;height:362px;background:var(--form-bg);border-radius:3px}
.lead-form h2{position:absolute;top:38px;left:0;width:100%;text-align:center;color:var(--white);font-family:"Kumbh Sans",sans-serif;font-weight:500;font-size:20px;line-height:29px;letter-spacing:.3px}
.field{position:absolute;background:var(--white);border-radius:2px;font-size:11px;color:#777;padding:12px 11px}
.f-name{left:26px;top:127px;width:175px;height:41px}
.f-number{left:221px;top:127px;width:175px;height:41px}
.f-address{left:26px;top:183px;width:370px;height:75px}
.btn-start{position:absolute;left:85px;top:288px;width:257px;height:47px;background:var(--green);border-radius:2px;text-align:center;line-height:47px;font-family:"Kumbh Sans",sans-serif;font-size:18px;font-weight:500;color:#1c1c1c}

/* steps */
.steps-title{left:0;width:1200px;top:830px;text-align:center;font-family:"Kumbh Sans",sans-serif;font-size:29px;font-weight:500;letter-spacing:.5px}
.steps-intro{left:197px;width:742px;top:886px;text-align:center;font-size:13.5px;line-height:23px;color:var(--muted)}
.steps-band{left:0;top:1009px;width:1200px;height:370px;background:var(--band)}
.step{position:absolute;top:1050px;width:240px;margin-left:-120px;text-align:center}
.step svg{display:block;margin:0 auto}
.step p{font-size:12.5px;line-height:17px;color:#555;margin-top:14px}

/* testimonials */
.testi-title{left:0;width:1200px;top:1450px;text-align:center;font-family:"Kumbh Sans",sans-serif;font-size:38px;font-weight:500}
.quote{position:absolute;width:430px;height:134px;padding:26px 60px;color:var(--white);font-family:"Raleway",sans-serif;font-size:16px;line-height:30px}
.quote::after{content:"";position:absolute;bottom:-26px;border-style:solid}
.quote-blue{left:178px;top:1545px;background:var(--blue)}
.quote-blue::after{left:292px;border-width:0 32px 26px 0;border-color:transparent var(--blue) transparent transparent}
.quote-green{left:584px;top:1571px;background:var(--green)}
.quote-green::after{left:292px;border-width:0 26px 26px 0;border-color:transparent var(--green) transparent transparent}
.author{position:absolute;display:flex;align-items:center;gap:14px;font-family:"Raleway",sans-serif}
.avatar{width:42px;height:42px;border-radius:50%;background:linear-gradient(160deg,#b39b88,#6d5446)}
.author b{display:block;font-weight:600;font-size:16px;color:#222}
.author span{display:block;font-size:12px;color:#888;margin-top:4px}
.arrow{position:absolute;width:42px;height:42px;border:1px solid #d5d5d5;border-radius:50%}

/* footer */
.footer{left:0;top:1874px;width:1200px;height:452px;background:var(--footer);font-family:"Roboto",sans-serif;color:var(--footer-text)}
.brand-footer{left:99px;top:70px;font-size:20px}
.about{left:98px;top:157px;width:226px;font-size:12px;line-height:26px}
.socials{left:98px;top:290px;display:flex;gap:11px}
.socials span{width:33px;height:33px;border-radius:50%;background:#2e343d}
.contact{position:absolute;top:50px;display:flex;align-items:flex-start;gap:16px;font-size:12px;line-height:20px}
.c-icon{width:33px;height:33px;border-radius:50%;background:#2e343d;flex:none;display:flex;align-items:center;justify-content:center}
.rule{position:absolute;height:1px;background:var(--footer-line)}
.col{position:absolute;top:156px}
.col h3{font-size:14px;font-weight:700;color:#d7dbe0;letter-spacing:.3px}
.col ul{list-style:none;margin-top:23px}
.col li{font-size:13px;line-height:31px;padding-left:17px;position:relative}
.col li::before{content:"";position:absolute;left:0;top:14px;width:5px;height:5px;border-radius:50%;background:#6a717b}
.col p{margin-top:23px;font-size:12px;line-height:26px;width:225px}
.email{left:849px;top:273px;width:226px;height:35px;background:#3a4048;font-size:11px;line-height:35px;padding-left:14px;color:#8a9199}
.subscribe{left:849px;top:316px;width:226px;height:36px;background:#0a86e0;color:var(--white);font-size:11px;font-weight:700;text-align:center;line-height:36px}
.copyright{left:0;width:1200px;top:415px;text-align:center;font-size:11.5px}
</style>
</head>
<body>

<svg class="hero-photo" viewBox="0 0 1200 670" role="img" aria-label="Photo of a technician in a safety vest installing rooftop solar panels under a blue sky">
  <defs>
    <linearGradient id="sky" x1="0" y1="0" x2="0" y2="1">
      <stop offset="0" stop-color="#1d3654"/>
      <stop offset=".3" stop-color="#6c8fb4"/>
      <stop offset=".55" stop-color="#3a4f7e"/>
      <stop offset="1" stop-color="#26346a"/>
    </linearGradient>
  </defs>
  <path d="M0 0H1200V575Q600 780 0 575Z" fill="url(#sky)"/>
</svg>

<div class="brand brand-header"><span class="brand-dot"></span>Terra Bright</div>
<nav class="nav">
  <a class="active">Home</a><a>Why</a><a>Partnerships</a><a>Morvalo Foundation</a><a>Blog</a><a>FAQ</a><a class="contact">Contact Us</a>
</nav>
<div class="abs hero-kicker">With Best Quality Solar Reception Cells</div>
<h1 class="abs hero-title">Terra Bright Energy</h1>

<form class="abs lead-form">
  <h2>ENTER YOUR ZIP CODE TO SEE<br>IF SOLAR WORKS FOR YOU.</h2>
  <div class="field f-name">Name</div>
  <div class="field f-number">Number</div>
  <div class="field f-address">Address</div>
  <div class="btn-start">Get Started</div>
</form>

<h2 class="abs steps-title">4 EASY STEPS TO GOING SOLAR</h2>
<p class="abs steps-intro">The world as it is heavily dependant on petrol, coal, wood and water for producing energy. We assume there is uninterrupted supply. There is n't! On the other hand, we have inexhaustible supply of solar energy. So why not rely more on solar energy ?</p>
<div class="abs steps-band"></div>

<div class="step" style="left:171px">
  <svg width="200" height="228" viewBox="0 0 200 228">
    <path d="M100 13a78 78 0 0 1 22 153L100 190 78 166A78 78 0 0 1 100 13Z" fill="var(--green-deep)"/>
    <circle cx="100" cy="91" r="66" fill="none" stroke="var(--yellow)" stroke-width="6"/>
    <circle cx="100" cy="202" r="4" fill="var(--green-deep)"/><circle cx="100" cy="216" r="4" fill="var(--green-deep)"/>
    <g fill="none" stroke="#fff" stroke-width="2.5" stroke-linecap="round">
      <path d="M72 96v-8a28 28 0 0 1 56 0v8"/><rect x="66" y="88" width="12" height="22" rx="5"/><rect x="122" y="88" width="12" height="22" rx="5"/><path d="M128 110q0 12-20 12"/>
    </g>
    <circle cx="158" cy="32" r="20" fill="var(--badge)" stroke="#fff" stroke-width="3"/>
    <text x="158" y="41" text-anchor="middle" font-family="Kumbh Sans,sans-serif" font-weight="700" font-size="24" fill="#fff">1</text>
  </svg>
  <p>Speak to a<br>solar consultant</p>
</div>

<div class="step" style="left:454px">
  <svg width="200" height="228" viewBox="0 0 200 228">
    <path d="M100 13a78 78 0 0 1 22 153L100 190 78 166A78 78 0 0 1 100 13Z" fill="var(--green-deep)"/>
    <circle cx="100" cy="91" r="66" fill="none" stroke="var(--yellow)" stroke-width="6"/>
    <circle cx="100" cy="202" r="4" fill="var(--green-deep)"/><circle cx="100" cy="216" r="4" fill="var(--green-deep)"/>
    <g fill="none" stroke="#fff" stroke-width="2.5" stroke-linejoin="round">
      <path d="M78 68h44l10 38H68Z"/><path d="M92 68l-4 38M108 68l4 38M74 81h52M71 94h58"/><path d="M92 118l30-20M96 122l30-20"/>
    </g>
    <circle cx="158" cy="32" r="20" fill="var(--badge)" stroke="#fff" stroke-width="3"/>
    <text x="158" y="41" text-anchor="middle" font-family="Kumbh Sans,sans-serif" font-weight="700" font-size="24" fill="#fff">2</text>
  </svg>
  <p>We'll design your<br>solar panel system</p>
</div>

<div class="step" style="left:725px">
  <svg width="200" height="228" viewBox="0 0 200 228">
    <path d="M100 13a78 78 0 0 1 22 153L100 190 78 166A78 78 0 0 1 100 13Z" fill="var(--green-deep)"/>
    <circle cx="100" cy="91" r="66" fill="none" stroke="var(--yellow)" stroke-width="6"/>
    <circle cx="100" cy="202" r="4" fill="var(--green-deep)"/><circle cx="100" cy="216" r="4" fill="var(--green-deep)"/>
    <g fill="none" stroke="#fff" stroke-width="2.5">
      <rect x="72" y="68" width="56" height="50" rx="3"/><path d="M72 82h56M84 62v12M116 62v12"/>
      <path d="M82 92h6M97 92h6M112 92h6M82 104h6M97 104h6"/><path d="M110 104l4 4 7-8" stroke-linecap="round"/>
    </g>
    <circle cx="158" cy="32" r="20" fill="var(--badge)" stroke="#fff" stroke-width="3"/>
    <text x="158" y="41" text-anchor="middle" font-family="Kumbh Sans,sans-serif" font-weight="700" font-size="24" fill="#fff">3</text>
  </svg>
  <p>Schedule your<br>1 day install</p>
</div>

<div class="step" style="left:997px">
  <svg width="200" height="228" viewBox="0 0 200 228">
    <path d="M100 13a78 78 0 0 1 22 153L100 190 78 166A78 78 0 0 1 100 13Z" fill="var(--green-deep)"/>
    <circle cx="100" cy="91" r="66" fill="none" stroke="var(--yellow)" stroke-width="6"/>
    <circle cx="100" cy="202" r="4" fill="var(--green-deep)"/><circle cx="100" cy="216" r="4" fill="var(--green-deep)"/>
    <g fill="none" stroke="#fff" stroke-width="2.5" stroke-linejoin="round">
      <ellipse cx="100" cy="94" rx="30" ry="22"/><path d="M82 116v8h8v-6M110 118v6h8v-8"/><path d="M92 74h16"/><path d="M130 90l6-2v10l-6-1"/>
    </g>
    <circle cx="158" cy="32" r="20" fill="var(--badge)" stroke="#fff" stroke-width="3"/>
    <text x="158" y="41" text-anchor="middle" font-family="Kumbh Sans,sans-serif" font-weight="700" font-size="24" fill="#fff">4</text>
  </svg>
  <p>Start saving on your<br>electricity bill</p>
</div>

<h2 class="abs testi-title">Client testimonials</h2>
<div class="arrow" style="left:92px;top:1651px"><svg width="40" height="40" viewBox="0 0 40 40"><path d="M23 14l-6 6 6 6" fill="none" stroke="#c8c8c8" stroke-width="1.5"/></svg></div>
<div class="arrow" style="left:1081px;top:1651px"><svg width="40" height="40" viewBox="0 0 40 40"><path d="M17 14l6 6-6 6" fill="none" stroke="#c8c8c8" stroke-width="1.5"/></svg></div>

<blockquote class="quote quote-blue">Lorem ipsum dolor sit amet, consectetur adipisicing elit. Enim, delectus atque odit esse harum! Saepe!</blockquote>
<blockquote class="quote quote-green">Lorem ipsum dolor sit amet, consectetur adipisicing elit. Enim, delectus atque odit esse harum! Saepe!</blockquote>
<div class="author" style="left:204px;top:1707px"><div class="avatar" role="img" aria-label="Portrait of John Doe"></div><div><b>John Doe</b><span>Web designer</span></div></div>
<div class="author" style="left:611px;top:1734px"><div class="avatar" role="img" aria-label="Portrait of Jessica Doe"></div><div><b>Jessica Doe</b><span>&nbsp;&nbsp;&nbsp;Developer</span></div></div>

<footer class="abs footer">
  <div class="brand brand-footer"><span class="brand-dot"></span>Terra Bright</div>
  <p class="abs about">We are Halverin, we industry factory company and provide you the best service and support comes register to receive service information</p>
  <div class="abs socials"><span></span><span></span><span></span><span></span><span></span></div>

  <div class="contact" style="left:349px"><div class="c-icon"><svg width="14" height="14" viewBox="0 0 14 14"><path d="M7 1a4 4 0 0 1 4 4c0 3-4 8-4 8S3 8 3 5a4 4 0 0 1 4-4Z" fill="none" stroke="#9aa0a8" stroke-width="1.3"/><circle cx="7" cy="5" r="1.4" fill="#9aa0a8"/></svg></div><div>48 Linden Grove - Westfield Park<br>Halden</div></div>
  <div class="contact" style="left:591px"><div class="c-icon"><svg width="14" height="14" viewBox="0 0 14 14"><path d="M3 1l2.5 3-1.5 1.5a8 8 0 0 0 4.5 4.5L10 8.5l3 2.5-1.5 2C6 13 1 8 1 2.5Z" fill="none" stroke="#9aa0a8" stroke-width="1.2"/></svg></div><div>(+10) 0555 210 734<br>(05) 550 7142 66</div></div>
  <div class="contact" style="left:832px"><div class="c-icon"><svg width="14" height="14" viewBox="0 0 14 14"><rect x="1.5" y="3" width="11" height="8" fill="none" stroke="#9aa0a8" stroke-width="1.2"/><path d="M1.5 3l5.5 4.5L12.5 3" fill="none" stroke="#9aa0a8" stroke-width="1.2"/></svg></div><div style="margin-top:6px">info@brightmail.test</div></div>

  <div class="rule" style="left:349px;top:122px;width:727px"></div>

  <div class="col" style="left:349px"><h3>QUICKLINK</h3><ul><li>Clean Energy</li><li>Solar Power</li><li>Repair Turbine</li><li>Energy Research</li></ul></div>
  <div class="col" style="left:600px"><h3>CUSTOMER CARE</h3><ul><li>Customer Service</li><li>Warranty Policy</li><li>Installation and Use</li><li>Contact Us</li></ul></div>
  <div class="col" style="left:849px"><h3>NEWSLETTER</h3><p>Sign up for our newsletter and follow us on social media</p></div>
  <div class="abs email">Email</div>
  <div class="abs subscribe">SUBSCRIBE</div>

  <div class="rule" style="left:98px;top:395px;width:978px"></div>
  <p class="abs copyright">Copyright © 2017 Terra Bright Energy.&nbsp; All rights reserved.</p>
</footer>

</body>
</html>
```